the kelvo pop

we have a product called the kelvo pop that we are looking for a label for the packaging - it is a weight loss chocolate bar for men only
its a low sugar low calorie healthy snack
our website is www.pindlefuel.com.au for more info about our company.
looking for a label design thats manly but also for the everyday person to eat
Our company colurs are blue, yellow and white.
Looking for something a bit quirky that grabs peoples attention.

```html
<!DOCTYPE html>
<html lang="en">
<head>
<meta charset="utf-8">
<title>The Kelvo Pop – Wrapper Label</title>
<link rel="stylesheet" href="https://fonts.googleapis.com/css2?family=Archivo+Black&family=Cabin:wght@700&family=Oswald:wght@600&display=swap">
<style>
  :root {
    --canvas: #ffffff;
    --chocolate: #4a1d12;
    --chocolate-light: #6b2e1a;
    --orange: #f39a1c;
    --orange-light: #fdbb2c;
    --badge: #f28c16;
    --tagline: #f7c23a;
    --brand-blue: #1f2c86;
    --white: #ffffff;
  }
  * { box-sizing: border-box; margin: 0; padding: 0; }
  html, body {
    width: 1200px;
    height: 1000px;
    overflow: hidden;
    background: var(--canvas);
  }
  .canvas {
    position: relative;
    width: 1200px;
    height: 1000px;
  }
  .label {
    position: absolute;
    left: 52px;
    top: 337px;
    width: 1096px;
    height: 326px;
    overflow: hidden;
    background: radial-gradient(ellipse at 45% 110%, var(--orange-light) 0%, var(--orange) 75%);
  }
  .label__sunburst {
    position: absolute;
    inset: 0;
    background: radial-gradient(ellipse at 50% 100%, rgba(255, 214, 90, 0.55) 0%, rgba(255, 214, 90, 0) 70%);
  }
  .label__top-band {
    position: absolute;
    left: 0;
    top: 0;
    width: 100%;
    height: 58px;
    background: var(--chocolate);
  }
  .label__drip {
    position: absolute;
    left: 0;
    top: 58px;
    width: 100%;
    height: 90px;
    background: linear-gradient(to bottom, var(--chocolate) 0%, rgba(107, 46, 26, 0.55) 45%, rgba(107, 46, 26, 0) 100%);
  }
  .label__tagline {
    position: absolute;
    left: 38px;
    top: 16px;
    font-family: "Cabin", sans-serif;
    font-weight: 700;
    font-size: 22px;
    letter-spacing: 0.5px;
    color: var(--tagline);
    text-transform: uppercase;
  }
  .label__product-name {
    position: absolute;
    left: 70px;
    top: 160px;
    font-family: "Archivo Black", sans-serif;
    font-size: 112px;
    line-height: 1;
    letter-spacing: -2px;
    color: var(--brand-blue);
    white-space: nowrap;
  }
  .label__badge {
    position: absolute;
    left: 886px;
    top: 115px;
    width: 186px;
    height: 186px;
  }
  .label__badge svg {
    position: absolute;
    inset: 0;
  }
  .label__badge-text {
    position: absolute;
    inset: 0;
    display: flex;
    flex-direction: column;
    align-items: center;
    justify-content: center;
    font-family: "Oswald", sans-serif;
    font-weight: 600;
    color: var(--white);
    line-height: 1.05;
    text-transform: uppercase;
  }
  .label__badge-lead { font-size: 42px; }
  .label__badge-line { font-size: 28px; }
</style>
</head>
<body>
<main class="canvas">
  <section class="label" aria-label="The Kelvo Pop wrapper label">
    <div class="label__sunburst" role="img" aria-label="Orange and yellow sunburst rays background"></div>
    <div class="label__top-band"></div>
    <div class="label__drip" role="img" aria-label="Melted chocolate dripping down from the top band"></div>

    <p class="label__tagline">A weight loss chocolate bar for men</p>

    <h1 class="label__product-name">KELVO POP</h1>

    <div class="label__badge">
      <svg viewBox="0 0 186 186" width="186" height="186" aria-hidden="true">
        <polygon fill="var(--badge)" points="93,3 104,17 119,7 125,24 142,18 143,36 161,35 156,52 173,56 163,71 178,81 164,93 178,105 163,115 173,130 156,134 161,151 143,150 142,168 125,162 119,179 104,169 93,183 82,169 67,179 61,162 44,168 43,150 25,151 30,134 13,130 23,115 8,105 22,93 8,81 23,71 13,56 30,52 25,35 43,36 44,18 61,24 67,7 82,17"/>
      </svg>
      <div class="label__badge-text">
        <span class="label__badge-lead">Low</span>
        <span class="label__badge-line">Sugar</span>
        <span class="label__badge-line">Calorie</span>
      </div>
    </div>
  </section>
</main>
</body>
</html>
```